Blue Heron IT Business Card - Clean, Simple

Need a simple, clean standard sized business card for an IT consulting business using existing logo and company colours. Background should be mainly white. Feel free to be creative but clean, simple, quiet design is preferred. Font is specified in logo but any sans serif fonts work.

Contact Information for card is as follows (doesn't need to be in this exact order):

Martin Calloway
Owner
martin@blueheronit.ca
705-391-2586
www.blueheronit.ca

Target Market(s)

Small to medium sized business.

Industry/Entity Type

IT Consulting

Contact Information for Business Card

Logo and contact info.

Font styles to use
Sans Serif

Colors
EE7325
F08F49
F5BC92
FAE3D3
FDF4ED

Requirements
Must have
• All white or mostly white background.

```html
<!DOCTYPE html>
<html lang="en">
<head>
<meta charset="utf-8">
<title>Blue Heron IT Business Card</title>
<link href="https://fonts.googleapis.com/css2?family=Montserrat:wght@400;500;700&display=swap" rel="stylesheet">
<style>
  :root {
    --stage: #ababab;
    --card-dark: #2f2f2f;
    --card-light: #ececec;
    --accent: #ee7325;
    --ink: #2a2a2a;
    --muted: #666666;
    --white: #ffffff;
  }
  * { margin: 0; padding: 0; box-sizing: border-box; }
  html, body {
    width: 1200px; height: 1000px; overflow: hidden;
    background: var(--stage);
    font-family: "Montserrat", Arial, sans-serif;
  }
  .canvas { position: relative; width: 1200px; height: 1000px; }
  .card {
    position: absolute; top: 194px; width: 351px; height: 612px;
  }
  .card--front { left: 227px; background: var(--card-dark); }
  .card--back { left: 644px; background: var(--card-light); }

  .brand { position: absolute; left: 0; right: 0; text-align: center; }
  .brand__mark {
    display: block; margin: 0 auto; border-radius: 50%;
    background: var(--accent);
  }
  .brand__name { display: block; font-weight: 500; white-space: nowrap; }

  .card--front .brand { top: 236px; }
  .card--front .brand__mark { width: 74px; height: 74px; }
  .card--front .brand__name {
    margin-top: 20px; font-size: 40px; color: var(--white); letter-spacing: -0.5px;
  }

  .contact { position: absolute; top: 226px; left: 0; right: 0; text-align: center; }
  .contact__name {
    font-size: 17px; font-weight: 700; color: var(--accent);
    letter-spacing: 0.6px; text-transform: uppercase; line-height: 22px;
  }
  .contact__role { font-size: 16px; color: var(--ink); line-height: 20px; }
  .contact__divider {
    display: flex; align-items: center; justify-content: center;
    gap: 4px; margin-top: 14px; height: 28px;
  }
  .contact__rule { width: 50px; height: 2px; background: var(--accent); margin: 0 4px; }
  .contact__icon {
    width: 27px; height: 27px; border-radius: 50%;
    background: var(--accent); border: 2px solid var(--white);
    display: flex; align-items: center; justify-content: center;
  }
  .contact__list { list-style: none; margin-top: 8px; }
  .contact__list li { font-size: 16.5px; color: var(--muted); line-height: 21px; }

  .card--back .brand { top: 468px; }
  .card--back .brand__mark { width: 40px; height: 40px; }
  .card--back .brand__name {
    margin-top: 10px; font-size: 23px; color: var(--ink); letter-spacing: -0.3px;
  }
</style>
</head>
<body>
<main class="canvas">
  <section class="card card--front">
    <div class="brand">
      <span class="brand__mark"></span>
      <span class="brand__name">Blue Heron IT</span>
    </div>
  </section>

  <section class="card card--back">
    <div class="contact">
      <p class="contact__name">Martin Calloway</p>
      <p class="contact__role">Owner</p>
      <div class="contact__divider">
        <span class="contact__rule"></span>
        <span class="contact__icon" aria-label="Phone">
          <svg width="13" height="13" viewBox="0 0 24 24"><path fill="#fff" d="M6.6 10.8a15 15 0 0 0 6.6 6.6l2.2-2.2c.3-.3.7-.4 1-.2 1.1.4 2.3.6 3.6.6.6 0 1 .4 1 1V20c0 .6-.4 1-1 1C10.6 21 3 13.4 3 4c0-.6.4-1 1-1h3.5c.6 0 1 .4 1 1 0 1.3.2 2.5.6 3.6.1.3 0 .7-.2 1z"/></svg>
        </span>
        <span class="contact__icon" aria-label="Email">
          <svg width="13" height="13" viewBox="0 0 24 24"><rect x="2" y="5" width="20" height="14" rx="1" fill="none" stroke="#fff" stroke-width="2"/><path d="M2 6l10 7 10-7" fill="none" stroke="#fff" stroke-width="2"/></svg>
        </span>
        <span class="contact__icon" aria-label="Website">
          <svg width="13" height="13" viewBox="0 0 24 24" fill="none" stroke="#fff" stroke-width="2"><circle cx="12" cy="12" r="9"/><ellipse cx="12" cy="12" rx="4" ry="9"/><path d="M3 12h18M5 7h14M5 17h14"/></svg>
        </span>
        <span class="contact__rule"></span>
      </div>
      <ul class="contact__list">
        <li>(705) 391-2586</li>
        <li>martin@blueheronit.ca</li>
        <li>www.blueheronit.ca</li>
      </ul>
    </div>
    <div class="brand">
      <span class="brand__mark"></span>
      <span class="brand__name">Blue Heron IT</span>
    </div>
  </section>
</main>
</body>
</html>
```